Fenmarrow brand new master design

Company Background:
The company Fenmarrow was founded in March 2019 and deals with the IT of the smallest companies. Unlike the PC specialist, no server is needed. Our motto is "just work". This motto aims to make it easy for the user to work without having to deal with the problems of PCs or a main computer.

This project:
We would like to create a Powerpoint Master wich makes us able to create future presentations. We'll need a design to ge it done. We are looking for a design aligned with our website and logo.

Target Market(s)

In a more complicated IT infrastructure it is even harder for small companies to maintain it. Even plumbers, electricians should be able to get a secure and reliable IT infrastructure. We are targeting companies between 1 and 15 IT users. Our customers do not have any ERP software that's just so simple. There is no need to have things like a server onsite anymore. We are providing the service from a safe and secure location within Germany.

Industry/Entity Type

It Company

Other font styles liked:
• Raleway

Requirements
Must have
• What we need to be in the master:
- Title Page (first slide)
- Table of content page
- Subtopic title page (Title with underline)
- Content-PAge with bullet points
- Content split bullet-points and image

We are using Raleway Google font.
Logos attached. Our website: www.fenmarrow.de
Must be aligned to our website and logo.
Nice to have
• selected Stock image gallery

```html
<!DOCTYPE html>
<html lang="en">
<head>
<meta charset="utf-8">
<title>Fenmarrow – Presentation Master</title>
<link href="https://fonts.googleapis.com/css2?family=Raleway:wght@300;400;500;600;700&display=swap" rel="stylesheet">
<style>
:root{
  --blue:#0b70bd;
  --blue-text:#1766b0;
  --navy:#1d4d9c;
  --panel:#efefef;
  --muted:#9aa8bf;
  --body:#3f6fae;
  --white:#ffffff;
}
*{box-sizing:border-box;margin:0;padding:0}
html,body{width:771px;height:1200px;overflow:hidden;background:var(--white)}
body{font-family:"Raleway",sans-serif;position:relative}
.slide{position:absolute;width:344px;height:193px;background:var(--white);overflow:hidden;box-shadow:0 5px 9px rgba(0,0,0,.16),0 0 2px rgba(0,0,0,.06)}
.slide > *{position:absolute}
.col-l{left:26px}.col-r{left:402px}
.row-1{top:58px}.row-2{top:281px}.row-3{top:504px}.row-4{top:727px}.row-5{top:950px}

/* shared header & footer */
.head-bar{left:0;top:17.5px;width:6.5px;height:25px;background:var(--blue)}
.slide-title{left:17.5px;top:20.5px;font-size:11.8px;font-weight:400;color:var(--blue-text);white-space:nowrap}
.slide-sub{left:17.5px;top:37px;font-size:3.8px;color:var(--muted);white-space:nowrap}
.brand-mark{right:17px;top:26px;font-size:7px;font-weight:600;color:var(--blue);letter-spacing:.4px}
.foot-line{left:188.5px;top:183.5px;width:129px;height:.6px;background:var(--blue)}
.page-no{left:320px;top:178.5px;width:11px;height:10.5px;background:var(--navy);color:var(--white);font-size:3.6px;display:flex;align-items:center;justify-content:center;border-radius:1px}

/* title slide */
.corner-block{background:var(--blue)}
.title-panel{background:var(--panel)}
.brand-box{left:15px;top:85px;width:92.5px;height:23px;background:var(--blue);color:var(--white);font-size:9px;font-weight:600;letter-spacing:.8px;display:flex;align-items:center;justify-content:center;box-shadow:1px 1px 2px rgba(0,0,0,.25)}
.hero-title{left:46px;top:110px;font-size:17.5px;font-weight:400;color:var(--blue-text);letter-spacing:.2px}
.hero-rule{left:46px;width:216px;height:.6px;background:var(--blue)}
.hero-sub{left:46px;top:147px;font-size:8.4px;color:var(--blue-text)}
.base-line{left:0;top:181px;width:262px;height:.5px;background:#cfcfcf}
.date-line{left:262px;top:181px;width:22px;height:.5px;background:var(--white)}
.date-text{left:288px;top:177.5px;font-size:6.2px;color:var(--white)}

/* agenda */
.agenda-list{list-style:none}
.agenda-list li{position:absolute;font-size:7.4px;color:var(--blue-text);white-space:nowrap}
.agenda-list .num{display:inline-block;width:12.5px;color:var(--blue-text);font-size:6.6px}

/* text columns */
.text-col{font-size:3.55px;line-height:6.6px;color:var(--body);text-align:left}
.text-col p{margin-bottom:6.6px}
.text-wide{text-align:justify}

/* feature bullets */
.feature{display:flex;gap:9px;width:150px}
.icon-tile{flex:none;width:15px;height:15px;border-radius:2.5px;background:var(--blue);display:flex;align-items:center;justify-content:center}
.icon-tile svg{width:10px;height:10px}
.feature h3{font-size:6.2px;font-weight:700;color:var(--blue-text);margin-top:.5px}
.feature p{font-size:3.7px;line-height:4.4px;color:var(--body);text-align:justify;width:111px}
.photo{background:linear-gradient(135deg,#e9f1f7 0%,#b9d2e4 45%,#4f7596 75%,#22364d 100%)}
.photo-work{background:linear-gradient(120deg,#f2f3f2 0%,#dfe3e6 50%,#9eb6cf 80%,#7e94ad 100%)}
.photo-strip{background:var(--navy)}

/* numbered grid */
.step{width:95px}
.step-head{display:flex;align-items:center;gap:9px}
.step-num{width:15px;height:14.5px;background:var(--blue);color:var(--white);font-size:6.5px;display:flex;align-items:center;justify-content:center;border-radius:1px}
.step h3{font-size:6.2px;font-weight:700;color:var(--blue-text)}
.step p{margin-top:5.5px;font-size:3.7px;line-height:5px;color:var(--body);text-align:justify;padding-left:1.5px}

/* circle bullets */
.circle-item{display:flex;align-items:center;gap:5px;width:130px}
.circle-icon{flex:none;width:29px;height:29px;border-radius:50%;background:var(--blue);display:flex;align-items:center;justify-content:center;box-shadow:0 1px 2px rgba(0,0,0,.25)}
.circle-icon svg{width:13px;height:13px}
.circle-item h3{font-size:7.4px;font-weight:400;color:var(--blue-text);line-height:8px}
.circle-item p{font-size:3.7px;line-height:4.6px;color:var(--body)}

/* contact */
.contact-photo{left:0;top:0;width:152px;height:193px;background:linear-gradient(160deg,#6a9fd0 0%,#3e80c2 45%,#2a6db4 75%,#205fa6 100%)}
.contact-title{left:185px;top:48px;font-size:15px;font-weight:500;color:var(--blue-text)}
.contact-list{list-style:none;left:187px;top:74px}
.contact-list li{display:flex;align-items:center;gap:5.5px;height:15.5px;margin-bottom:3.3px;font-size:4.3px;color:var(--body);line-height:5px}
.contact-icon{flex:none;width:15px;height:15.5px;border:.8px solid var(--blue);border-radius:2px;display:flex;align-items:center;justify-content:center}
.contact-icon svg{width:9px;height:9px}

/* closing */
.closing-panel{left:0;top:0;width:116px;height:193px;background:var(--panel)}
.closing-band{left:0;top:106px;width:249.5px;height:70px;background:var(--blue)}
.closing-title{left:0;width:227px;top:119px;text-align:center;font-size:16px;font-weight:400;color:var(--white);letter-spacing:.3px}
.closing-rule{left:21.5px;top:142px;width:206px;height:.6px;background:var(--white)}
.closing-sub{left:0;width:241px;top:148px;text-align:center;font-size:8.3px;color:var(--white)}
</style>
</head>
<body>

<svg width="0" height="0" style="position:absolute" aria-hidden="true">
  <defs>
    <symbol id="i-globe" viewBox="0 0 24 24"><g fill="none" stroke="#fff" stroke-width="2"><circle cx="12" cy="12" r="9"/><ellipse cx="12" cy="12" rx="4" ry="9"/><path d="M3 12h18"/></g></symbol>
    <symbol id="i-megaphone" viewBox="0 0 24 24"><path d="M3 9h5l10-5v16L8 15H3z" fill="#fff"/><path d="M7 15l2 6h3l-2-6" fill="#fff"/></symbol>
    <symbol id="i-rocket" viewBox="0 0 24 24"><path d="M20 4c-6 0-10 3-12 8l4 4c5-2 8-6 8-12z" fill="#fff"/><path d="M8 12l-4 1 2-4 4-1zM12 16l-1 4 4-2 1-4z" fill="#fff"/><path d="M6 16l-3 5 5-3" fill="#fff"/></symbol>
    <symbol id="i-pulse" viewBox="0 0 24 24"><polyline points="2,13 6,13 8,7 11,19 14,5 16,13 22,13" fill="none" stroke="#fff" stroke-width="2" stroke-linejoin="round"/></symbol>
    <symbol id="i-key" viewBox="0 0 24 24"><g fill="none" stroke="#fff" stroke-width="2.4"><circle cx="8" cy="8" r="4"/><path d="M11 11l9 9M16 16l2-2M18 18l2-2"/></g></symbol>
    <symbol id="i-spark" viewBox="0 0 24 24"><g stroke="#fff" stroke-width="2" stroke-linecap="round"><path d="M12 3v5M12 16v5M3 12h5M16 12h5M5.6 5.6l3.5 3.5M14.9 14.9l3.5 3.5M5.6 18.4l3.5-3.5M14.9 9.1l3.5-3.5"/></g></symbol>
    <symbol id="i-bell" viewBox="0 0 24 24"><path d="M12 3a6 6 0 0 0-6 6v5l-2 3h16l-2-3V9a6 6 0 0 0-6-6z" fill="#fff"/><circle cx="12" cy="20" r="2" fill="#fff"/></symbol>
    <symbol id="i-tools" viewBox="0 0 24 24"><g stroke="#fff" stroke-width="2.4" stroke-linecap="round"><path d="M4 4l16 16M20 4L4 20"/></g></symbol>
    <symbol id="i-anchor" viewBox="0 0 24 24"><g fill="none" stroke="#fff" stroke-width="2"><circle cx="12" cy="5" r="2"/><path d="M12 7v14M8 11h8M4 14a8 7 0 0 0 16 0"/></g></symbol>
    <symbol id="i-pin" viewBox="0 0 24 24"><path d="M12 2a7 7 0 0 0-7 7c0 5 7 13 7 13s7-8 7-13a7 7 0 0 0-7-7zm0 10a3 3 0 1 1 0-6 3 3 0 0 1 0 6z" fill="#0b70bd"/></symbol>
    <symbol id="i-phone" viewBox="0 0 24 24"><path d="M6 3l3 0 2 5-2 2c1 2 3 4 5 5l2-2 5 2v3c0 1-1 2-2 2C10 20 4 14 4 5c0-1 1-2 2-2z" fill="none" stroke="#0b70bd" stroke-width="2"/></symbol>
    <symbol id="i-mobile" viewBox="0 0 24 24"><rect x="7" y="2" width="10" height="20" rx="2" fill="none" stroke="#0b70bd" stroke-width="2"/><circle cx="12" cy="18" r="1" fill="#0b70bd"/></symbol>
    <symbol id="i-mail" viewBox="0 0 24 24"><rect x="3" y="6" width="18" height="12" fill="#0b70bd"/><path d="M3 6l9 7 9-7" fill="none" stroke="#fff" stroke-width="1.6"/></symbol>
    <symbol id="i-link" viewBox="0 0 24 24"><g fill="none" stroke="#0b70bd" stroke-width="2"><path d="M10 14l4-4"/><path d="M8 12l-3 3a3 3 0 0 0 4 4l3-3M16 12l3-3a3 3 0 0 0-4-4l-3 3"/></g></symbol>
  </defs>
</svg>

<!-- 1 Title -->
<section class="slide col-l row-1">
  <div class="title-panel" style="left:28.5px;top:74.5px;width:316px;height:97px"></div>
  <div class="corner-block" style="left:262px;top:0;width:82px;height:74.5px"></div>
  <div class="brand-box">FENMARROW</div>
  <h1 class="hero-title">FENMARROW</h1>
  <div class="hero-rule" style="top:142px"></div>
  <p class="hero-sub">Business PowerPoint Presentation</p>
  <div class="base-line"></div>
  <div class="corner-block" style="left:262px;top:171.5px;width:82px;height:21.5px"></div>
  <div class="date-line"></div>
  <span class="date-text">June 4 , 2020</span>
</section>

<!-- 2 Agenda -->
<section class="slide col-r row-1">
  <div class="title-panel" style="left:28.5px;top:19.5px;width:316px;height:154px"></div>
  <div class="corner-block" style="left:262px;top:0;width:82px;height:19.5px"></div>
  <div class="brand-box" style="top:30px">FENMARROW</div>
  <h1 class="hero-title" style="top:64px">Agenda</h1>
  <div class="hero-rule" style="top:87px"></div>
  <ol class="agenda-list" style="left:0;top:0">
    <li style="left:47px;top:94px"><span class="num">1.</span>Opening</li>
    <li style="left:47px;top:107px"><span class="num">2.</span>Topic ABC</li>
    <li style="left:47px;top:120px"><span class="num">3.</span>Topic DEF</li>
    <li style="left:47px;top:133px"><span class="num">4.</span>Topic GHJ</li>
    <li style="left:47px;top:146px"><span class="num">5.</span>Topic KLM</li>
    <li style="left:47px;top:158.5px"><span class="num">6.</span>Break Time</li>
    <li style="left:152.5px;top:94px"><span class="num">7.</span>Practice</li>
    <li style="left:152.5px;top:107px"><span class="num">8.</span>Exercise 1</li>
    <li style="left:152.5px;top:120px"><span class="num">9.</span>Discussion</li>
    <li style="left:152.5px;top:133px"><span class="num">10.</span>Exercise 2</li>
    <li style="left:152.5px;top:146px"><span class="num">11.</span>Discussion</li>
    <li style="left:152.5px;top:158.5px"><span class="num">12.</span>Closing</li>
  </ol>
  <div class="base-line"></div>
  <div class="corner-block" style="left:262px;top:173.5px;width:82px;height:19.5px"></div>
  <div class="date-line" style="width:63px"></div>
</section>

<!-- 3 Title with underline, two columns -->
<section class="slide col-l row-2">
  <div class="head-bar"></div>
  <h2 class="slide-title">Title with underline - title here</h2>
  <p class="slide-sub">Subtopic title page here &nbsp;your subtitle here</p>
  <span class="brand-mark">FENMARROW</span>
  <div class="text-col" style="left:15px;top:49px;width:148px">
    <p>Lorem ipsum is simply dummy text of the printing and typesetting industry. Lorem ipsum has been the industry's standard dummy text ever since the 1500s, when an unknown printer took a galley of type and scrambled it to make a type specimen book. It has survived not only five centuries, but also the leap into electronic typesetting, remaining essentially unchanged. It was popularised in the 1960s with the release of sheets containing Lorem ipsum passages.</p>
    <p>Contrary to popular belief, Lorem ipsum is not simply random text. It has roots in a piece of classical Latin literature from 45 BC, making it over 2000 years old. A Latin professor looked up one of the more obscure Latin words, consectetur, from a Lorem ipsum passage, and going through the cites of the word in classical literature, discovered the undoubtable source.</p>
  </div>
  <div class="text-col" style="left:177px;top:49px;width:148px">
    <p>Lorem ipsum is simply dummy text of the printing and typesetting industry. Lorem ipsum has been the industry's standard dummy text ever since the 1500s, when an unknown printer took a galley of type and scrambled it to make a type specimen book. It has survived not only five centuries, but also the leap into electronic typesetting, remaining essentially unchanged. It was popularised in the 1960s with the release of sheets containing Lorem ipsum passages.</p>
    <p>Contrary to popular belief, Lorem ipsum is not simply random text. It has roots in a piece of classical Latin literature from 45 BC, making it over 2000 years old. A Latin professor looked up one of the more obscure Latin words, consectetur, from a Lorem ipsum passage, and going through the cites of the word in classical literature, discovered the undoubtable source.</p>
  </div>
  <div class="foot-line"></div><span class="page-no">3</span>
</section>

<!-- 4 Title with underline, one column -->
<section class="slide col-r row-2">
  <div class="head-bar"></div>
  <h2 class="slide-title">Title with underline - title here</h2>
  <p class="slide-sub">Subtopic title page here &nbsp;your subtitle here</p>
  <span class="brand-mark">FENMARROW</span>
  <div class="text-col text-wide" style="left:15px;top:55px;width:311px">
    <p>Lorem ipsum is simply dummy text of the printing and typesetting industry. Lorem ipsum has been the industry's standard dummy text ever since the 1500s, when an unknown printer took a galley of type and scrambled it to make a type specimen book. It has survived not only five centuries, but also the leap into electronic typesetting, remaining essentially unchanged. It was popularised in the 1960s with the release of sheets containing Lorem ipsum passages.</p>
    <p>Contrary to popular belief, Lorem ipsum is not simply random text. It has roots in a piece of classical Latin literature from 45 BC, making it over 2000 years old. A Latin professor looked up one of the more obscure Latin words, consectetur, from a Lorem ipsum passage, and going through the cites of the word in classical literature, discovered the undoubtable source.</p>
    <p>Lorem ipsum is simply dummy text of the printing and typesetting industry. Lorem ipsum has been the industry's standard dummy text ever since the 1500s, when an unknown printer took a galley of type and scrambled it to make a type specimen book. It has survived not only five centuries, but also the leap into electronic typesetting, remaining essentially unchanged. It was popularised in the 1960s with the release of sheets containing Lorem ipsum passages.</p>
  </div>
  <div class="foot-line"></div><span class="page-no">4</span>
</section>

<!-- 5 Split: bullets left, image right -->
<section class="slide col-l row-3">
  <div class="head-bar"></div>
  <h2 class="slide-title">Content split bullet-points and image</h2>
  <p class="slide-sub">Subtopic title page here &nbsp;your subtitle here</p>
  <span class="brand-mark">FENMARROW</span>
  <div class="feature" style="left:17.5px;top:56px"><span class="icon-tile"><svg><use href="#i-globe"/></svg></span><div><h3>Lorem Ipsum</h3><p>It is a long established fact that a reader will be distracted by the readable content of a page when</p></div></div>
  <div class="feature" style="left:17.5px;top:87.5px"><span class="icon-tile"><svg><use href="#i-megaphone"/></svg></span><div><h3>Lorem Ipsum</h3><p>It is a long established fact that a reader will be distracted by the readable content of a page when</p></div></div>
  <div class="feature" style="left:17.5px;top:119px"><span class="icon-tile"><svg><use href="#i-rocket"/></svg></span><div><h3>Lorem Ipsum</h3><p>It is a long established fact that a reader will be distracted by the readable content of a page when</p></div></div>
  <div class="feature" style="left:17.5px;top:150.5px"><span class="icon-tile"><svg><use href="#i-pulse"/></svg></span><div><h3>Lorem Ipsum</h3><p>It is a long established fact that a reader will be distracted by the readable content of a page when</p></div></div>
  <div class="photo" style="left:177.5px;top:50.5px;width:146.5px;height:121px" role="img" aria-label="Photo: a hand holding a glowing security shield with a padlock"></div>
  <div class="foot-line"></div><span class="page-no">5</span>
</section>

<!-- 6 Split: image left, bullets right -->
<section class="slide col-r row-3">
  <div class="head-bar"></div>
  <h2 class="slide-title">Content split bullet-points and image</h2>
  <p class="slide-sub">Subtopic title page here &nbsp;your subtitle here</p>
  <span class="brand-mark">FENMARROW</span>
  <div class="photo-work" style="left:17.5px;top:51.5px;width:146px;height:121px" role="img" aria-label="Photo: a smiling man working on a laptop in a bright office"></div>
  <div class="photo-strip" style="left:17.5px;top:51.5px;width:16px;height:121px"></div>
  <div class="feature" style="left:189px;top:56px"><span class="icon-tile"><svg><use href="#i-globe"/></svg></span><div><h3>Lorem Ipsum</h3><p>It is a long established fact that a reader will be distracted by the readable content of a page when</p></div></div>
  <div class="feature" style="left:189px;top:87.5px"><span class="icon-tile"><svg><use href="#i-megaphone"/></svg></span><div><h3>Lorem Ipsum</h3><p>It is a long established fact that a reader will be distracted by the readable content of a page when</p></div></div>
  <div class="feature" style="left:189px;top:119px"><span class="icon-tile"><svg><use href="#i-rocket"/></svg></span><div><h3>Lorem Ipsum</h3><p>It is a long established fact that a reader will be distracted by the readable content of a page when</p></div></div>
  <div class="feature" style="left:189px;top:150.5px"><span class="icon-tile"><svg><use href="#i-pulse"/></svg></span><div><h3>Lorem Ipsum</h3><p>It is a long established fact that a reader will be distracted by the readable content of a page when</p></div></div>
  <div class="foot-line"></div><span class="page-no">6</span>
</section>

<!-- 7 Numbered bullet grid -->
<section class="slide col-l row-4">
  <div class="head-bar"></div>
  <h2 class="slide-title">Content-Page with bullet points</h2>
  <p class="slide-sub">Subtopic title page here , your subtitle here</p>
  <span class="brand-mark">FENMARROW</span>
  <div class="step" style="left:17.5px;top:56.5px"><div class="step-head"><span class="step-num">1</span><h3>Lorem Ipsum</h3></div><p>It is a long established fact that a reader will be distracted by the readable content of a page when looking at its layout. The point of using Lorem Ipsum is that it has a more-or-less normal distribution of letters, as opposed</p></div>
  <div class="step" style="left:124px;top:56.5px"><div class="step-head"><span class="step-num">2</span><h3>Lorem Ipsum</h3></div><p>It is a long established fact that a reader will be distracted by the readable content of a page when looking at its layout. The point of using Lorem Ipsum is that it has a more-or-less normal distribution of letters, as opposed</p></div>
  <div class="step" style="left:232.5px;top:56.5px"><div class="step-head"><span class="step-num">3</span><h3>Lorem Ipsum</h3></div><p>It is a long established fact that a reader will be distracted by the readable content of a page when looking at its layout. The point of using Lorem Ipsum is that it has a more-or-less normal distribution of letters, as opposed</p></div>
  <div class="step" style="left:17.5px;top:117.5px"><div class="step-head"><span class="step-num">4</span><h3>Lorem Ipsum</h3></div><p>It is a long established fact that a reader will be distracted by the readable content of a page when looking at its layout. The point of using Lorem Ipsum is that it has a more-or-less normal distribution of letters, as opposed</p></div>
  <div class="step" style="left:124px;top:117.5px"><div class="step-head"><span class="step-num">5</span><h3>Lorem Ipsum</h3></div><p>It is a long established fact that a reader will be distracted by the readable content of a page when looking at its layout. The point of using Lorem Ipsum is that it has a more-or-less normal distribution of letters, as opposed</p></div>
  <div class="step" style="left:232.5px;top:117.5px"><div class="step-head"><span class="step-num">6</span><h3>Lorem Ipsum</h3></div><p>It is a long established fact that a reader will be distracted by the readable content of a page when looking at its layout. The point of using Lorem Ipsum is that it has a more-or-less normal distribution of letters, as opposed</p></div>
  <div class="foot-line"></div><span class="page-no">7</span>
</section>

<!-- 8 Circle icon bullets -->
<section class="slide col-r row-4">
  <div class="head-bar"></div>
  <h2 class="slide-title">Content-Page with bullet points</h2>
  <p class="slide-sub">Subtopic title page here , your subtitle here</p>
  <span class="brand-mark">FENMARROW</span>
  <div class="circle-item" style="left:40px;top:59px"><span class="circle-icon"><svg><use href="#i-key"/></svg></span><div><h3>Lorem Ipsum</h3><p>Is ria qui del ium aut ex et estrum nonsequis<br>volupta doluptas illuptas</p></div></div>
  <div class="circle-item" style="left:40px;top:96.5px"><span class="circle-icon"><svg><use href="#i-bell"/></svg></span><div><h3>Lorem Ipsum</h3><p>Is ria qui del ium aut ex et estrum nonsequis<br>volupta doluptas illuptas</p></div></div>
  <div class="circle-item" style="left:40px;top:133px"><span class="circle-icon"><svg><use href="#i-anchor"/></svg></span><div><h3>Lorem Ipsum</h3><p>Is ria qui del ium aut ex et estrum nonsequis<br>volupta doluptas illuptas</p></div></div>
  <div class="circle-item" style="left:176px;top:59px"><span class="circle-icon"><svg><use href="#i-spark"/></svg></span><div><h3>Lorem Ipsum</h3><p>Is ria qui del ium aut ex et estrum nonsequis<br>volupta doluptas illuptas</p></div></div>
  <div class="circle-item" style="left:176px;top:96.5px"><span class="circle-icon"><svg><use href="#i-tools"/></svg></span><div><h3>Lorem Ipsum</h3><p>Is ria qui del ium aut ex et estrum nonsequis<br>volupta doluptas illuptas</p></div></div>
  <div class="circle-item" style="left:176px;top:133px"><span class="circle-icon"><svg><use href="#i-megaphone"/></svg></span><div><h3>Norvale Global</h3><p>Is ria qui del ium aut ex et estrum nonsequis<br>volupta doluptas illuptas</p></div></div>
  <div class="foot-line"></div><span class="page-no">8</span>
</section>

<!-- 9 Contact -->
<section class="slide col-l row-5">
  <div class="contact-photo" role="img" aria-label="Blue-tinted photo: two colleagues looking at documents together"></div>
  <span class="brand-mark" style="top:28px">FENMARROW</span>
  <h2 class="contact-title">Contact Us</h2>
  <ul class="contact-list">
    <li><span class="contact-icon"><svg><use href="#i-pin"/></svg></span>Lorem ipsum dolor sit amet, consectetuer<br>adipiscing elit.</li>
    <li><span class="contact-icon"><svg><use href="#i-phone"/></svg></span>+1 234 567 890</li>
    <li><span class="contact-icon"><svg><use href="#i-mobile"/></svg></span>+1 234 567 890</li>
    <li><span class="contact-icon"><svg><use href="#i-mail"/></svg></span>name@domainname.com</li>
    <li><span class="contact-icon"><svg><use href="#i-link"/></svg></span>www.domainname.com</li>
  </ul>
  <div class="foot-line"></div><span class="page-no">9</span>
</section>

<!-- 10 Closing -->
<section class="slide col-r row-5">
  <div class="closing-panel"></div>
  <span class="brand-mark" style="top:28px">FENMARROW</span>
  <div class="closing-band"></div>
  <h2 class="closing-title">THANKS YOU</h2>
  <div class="closing-rule"></div>
  <p class="closing-sub">FENMARROW PRESENTATION</p>
</section>

</body>
</html>
```